Dovenmarch Luxury Landscapes

A landscape business card.

Target Market(s)

Middle aged and up. Professionals.

Industry/Entity Type

Landscape

Contact Information for Business Card

Thornbeck

Colors
0054AA
0677BA
7BADD7
CADEEF
E8F1F8
0094D4
00A9DD
6FCCEA
C7EBF8
E9F6FB

Requirements
Must have
• The color blue and silver be very attractive
Nice to have
• An embossed logo. A watermark of a plant or something that indicates that we are a landscape company in the background of the backside where list of services are offered. . List of services on the back.
Should not have
• Red, yellow, orange.

```html
<!DOCTYPE html>
<html lang="en">
<head>
<meta charset="utf-8">
<title>Dovenmarch Luxury Landscapes – Business Card</title>
<link rel="stylesheet" href="https://fonts.googleapis.com/css2?family=Montserrat:wght@400;500;700;800&display=swap">
<style>
  :root {
    --brand-blue: #3246a0;
    --brand-blue-deep: #28398a;
    --paper: #ffffff;
    --ink: #1f1f2a;
    --backdrop: #e9ecf2;
  }
  * { box-sizing: border-box; margin: 0; padding: 0; }
  html, body {
    width: 1200px; height: 800px; overflow: hidden;
    background: var(--backdrop);
    font-family: "Montserrat", sans-serif;
  }
  .stage {
    width: 1200px; height: 800px;
    display: flex; align-items: center; justify-content: center; gap: 30px;
  }
  .card {
    width: 560px; height: 320px; border-radius: 16px;
    position: relative; overflow: hidden;
    box-shadow: 0 10px 28px rgba(20, 30, 70, 0.18);
  }

  /* Back side */
  .card-back {
    background: var(--brand-blue);
    display: flex; align-items: center; justify-content: center;
  }
  .back-brand {
    color: var(--paper); font-weight: 800; text-align: center;
    text-transform: uppercase; line-height: 1.05;
  }
  .back-brand .brand-main { display: block; font-size: 46px; letter-spacing: 1px; }
  .back-brand .brand-sub { display: block; font-size: 19px; letter-spacing: 3px; }

  /* Front side */
  .card-front { background: var(--paper); }
  .front-brand {
    position: absolute; left: 34px; top: 34px;
    color: var(--brand-blue); font-weight: 800; text-transform: uppercase; line-height: 1;
  }
  .front-brand .brand-main { display: block; font-size: 58px; letter-spacing: 0.5px; }
  .front-brand .brand-sub { display: block; font-size: 25px; letter-spacing: 2.4px; margin-top: 4px; }

  .front-details {
    position: absolute; left: 34px; top: 150px; right: 30px;
    display: flex; align-items: center;
  }
  .person { text-align: right; padding-right: 18px; }
  .person-name { color: var(--brand-blue); font-weight: 800; font-size: 22px; }
  .person-role { color: var(--ink); font-weight: 500; font-size: 13px; margin-top: 2px; }
  .divider { width: 1px; height: 66px; background: var(--brand-blue); }
  .contacts { list-style: none; padding-left: 18px; }
  .contacts li {
    display: flex; align-items: center; gap: 10px;
    color: var(--ink); font-size: 12.5px; font-weight: 500; line-height: 22px;
  }
  .contacts svg { width: 14px; height: 14px; fill: var(--brand-blue); flex: none; }

  .address-band {
    position: absolute; left: 0; right: 0; bottom: 22px; height: 42px;
    background: var(--brand-blue);
    display: flex; align-items: center; justify-content: center;
    color: var(--paper); font-size: 13px; font-weight: 500; letter-spacing: 0.3px;
  }
  .base-strip {
    position: absolute; left: 0; right: 0; bottom: 0; height: 16px;
    background: var(--brand-blue);
  }
</style>
</head>
<body>
<main class="stage">

  <section class="card card-back" aria-label="Card back">
    <p class="back-brand">
      <span class="brand-main">Dovenmarch</span>
      <span class="brand-sub">Luxury Landscapes</span>
    </p>
  </section>

  <section class="card card-front" aria-label="Card front">
    <p class="front-brand">
      <span class="brand-main">Dovenmarch</span>
      <span class="brand-sub">Luxury Landscapes</span>
    </p>

    <div class="front-details">
      <div class="person">
        <p class="person-name">Marla Pendry</p>
        <p class="person-role">Managing Director</p>
      </div>
      <div class="divider"></div>
      <ul class="contacts">
        <li>
          <svg viewBox="0 0 24 24" aria-hidden="true"><path d="M6.6 10.8a15.1 15.1 0 0 0 6.6 6.6l2.2-2.2a1 1 0 0 1 1-.25 11.4 11.4 0 0 0 3.6.57 1 1 0 0 1 1 1V20a1 1 0 0 1-1 1A17 17 0 0 1 3 4a1 1 0 0 1 1-1h3.5a1 1 0 0 1 1 1c0 1.25.2 2.45.57 3.6a1 1 0 0 1-.25 1z"/></svg>
          902-555-LAWN
        </li>
        <li>
          <svg viewBox="0 0 24 24" aria-hidden="true"><path d="M2 5h20v14H2z" fill="none"/><path d="M2 5h20v2l-10 6L2 7zM2 9l10 6 10-6v10H2z"/></svg>
          hello@dovenmarch.com
        </li>
        <li>
          <svg viewBox="0 0 24 24" aria-hidden="true"><path d="M12 2a10 10 0 1 0 0 20 10 10 0 0 0 0-20zm6.9 6h-2.9a15.6 15.6 0 0 0-1.4-3.6A8 8 0 0 1 18.9 8zM12 4a14 14 0 0 1 1.9 4h-3.8A14 14 0 0 1 12 4zM4.3 14a8 8 0 0 1 0-4h3.4a16.5 16.5 0 0 0 0 4zm.8 2h2.9a15.6 15.6 0 0 0 1.4 3.6A8 8 0 0 1 5.1 16zM8 8H5.1a8 8 0 0 1 4.3-3.6A15.6 15.6 0 0 0 8 8zm4 12a14 14 0 0 1-1.9-4h3.8A14 14 0 0 1 12 20zm2.3-6H9.7a14.7 14.7 0 0 1 0-4h4.6a14.7 14.7 0 0 1 0 4zm.3 5.6A15.6 15.6 0 0 0 16 16h2.9a8 8 0 0 1-4.3 3.6zM16.3 14a16.5 16.5 0 0 0 0-4h3.4a8 8 0 0 1 0 4z"/></svg>
          www.dovenmarch.com
        </li>
      </ul>
    </div>

    <p class="address-band">18B Fernhollow Lane, Thornbeck, Nova Scotia, B3X 4K2</p>
    <div class="base-strip"></div>
  </section>

</main>
</body>
</html>
```